Design a powerpoint background using company logo/colours

We require a powerpoint background that incorporates our company colours and logo. I have attached the logo in various sizes.

Have fun and be imaginative

Our company colours are white and Red-236, Green-22 and Blue 86.
Please use these colours in designing the ppt background

Industry/Entity Type

It Company

Colors

Designer to choose colors to be used in the design.

```html
<!DOCTYPE html>
<html lang="en">
<head>
<meta charset="utf-8">
<title>Orvastel — Title Slide</title>
<link rel="stylesheet" href="https://fonts.googleapis.com/css2?family=Carlito:wght@400;700&display=swap">
<style>
  :root {
    --brand-red: #e2044f;
    --brand-red-deep: #d8003f;
    --brand-pink: #ef6a88;
    --paper: #ffffff;
  }
  html, body {
    margin: 0;
    padding: 0;
    width: 1200px;
    height: 900px;
    overflow: hidden;
    background: var(--paper);
  }
  .slide {
    position: relative;
    width: 1200px;
    height: 900px;
    overflow: hidden;
    background: var(--paper);
    font-family: "Carlito", "Calibri", sans-serif;
  }
  .decor {
    position: absolute;
    inset: 0;
    width: 1200px;
    height: 900px;
  }
  .brand-name {
    position: absolute;
    left: 50px;
    top: 48px;
    margin: 0;
    font-weight: 700;
    font-size: 60px;
    line-height: 1;
    letter-spacing: -1px;
    color: var(--brand-red);
  }
  .title-badge {
    position: absolute;
    left: 350px;
    top: 170px;
    width: 500px;
    height: 500px;
    border-radius: 50%;
    background: var(--brand-red);
    text-align: center;
    color: var(--paper);
  }
  .title-badge::before {
    content: "";
    position: absolute;
    inset: 14px;
    border: 7px solid var(--paper);
    border-radius: 50%;
  }
  .slide-title {
    position: absolute;
    left: 0;
    right: 0;
    top: 124px;
    margin: 0;
    font-weight: 700;
    font-size: 72px;
    line-height: 87px;
    white-space: nowrap;
  }
  .slide-subtitle {
    position: absolute;
    left: 0;
    right: 0;
    top: 354px;
    margin: 0;
    font-weight: 400;
    font-size: 50px;
    line-height: 52px;
  }
</style>
</head>
<body>
<main class="slide">
  <svg class="decor" viewBox="0 0 720 540" preserveAspectRatio="none" aria-hidden="true">
    <defs>
      <linearGradient id="fade-top" x1="0" y1="0" x2="1" y2="1">
        <stop offset="0" stop-color="var(--brand-pink)"/>
        <stop offset="1" stop-color="var(--brand-red)"/>
      </linearGradient>
      <linearGradient id="fade-mid" x1="0" y1="0" x2="1" y2="1">
        <stop offset="0" stop-color="var(--brand-pink)"/>
        <stop offset="1" stop-color="var(--brand-red-deep)"/>
      </linearGradient>
      <linearGradient id="fade-corner" x1="1" y1="0" x2="0" y2="1">
        <stop offset="0" stop-color="var(--brand-red)"/>
        <stop offset="1" stop-color="var(--brand-red-deep)"/>
      </linearGradient>
      <linearGradient id="fade-left" x1="0" y1="0" x2="1" y2="1">
        <stop offset="0" stop-color="var(--brand-pink)"/>
        <stop offset="1" stop-color="var(--brand-red)"/>
      </linearGradient>
    </defs>
    <polygon class="shard shard-top" points="618,0 720,0 720,102" fill="url(#fade-top)"/>
    <polygon class="shard shard-small" points="626,25 668,106 600,90" fill="var(--brand-red)"/>
    <polygon class="shard shard-band" points="594,158 720,86 720,160" fill="var(--brand-red-deep)"/>
    <polygon class="shard shard-mid" points="594,160 720,160 720,332" fill="url(#fade-mid)"/>
    <polygon class="shard shard-corner" points="490,540 720,298 720,540" fill="url(#fade-corner)"/>
    <polygon class="shard shard-left" points="0,390 72,315 72,390" fill="var(--brand-red)"/>
    <polygon class="shard shard-low" points="0,396 130,540 0,540" fill="url(#fade-left)"/>
  </svg>

  <p class="brand-name">Orvastel</p>

  <section class="title-badge">
    <h1 class="slide-title">YOUR TITLE<br>HERE</h1>
    <p class="slide-subtitle">SUBTITLE</p>
  </section>
</main>
</body>
</html>
```